Velvet Shakers business card

We would like a business card designed for our business velvet shakers

We need it to have 2 sides.

More information about the business can be found at www.velvetshakers-example.net

Industry/Entity Type

Business

```html
<!DOCTYPE html>
<html lang="en">
<head>
<meta charset="utf-8">
<title>Velvet Shakers business card</title>
<link rel="stylesheet" href="https://fonts.googleapis.com/css2?family=Open+Sans:ital,wght@0,400;0,700;1,700&display=swap">
<style>
  :root {
    --backdrop: #3a322e;
    --card-black: #141414;
    --card-black-soft: #1d1d1d;
    --gold: #d4b45a;
    --gold-light: #e9d48f;
    --gold-deep: #a8863a;
    --ink-dark: #1a1a1a;
    --muted-grey: #8a8a8a;
    --title-grey: #9a9a9a;
  }
  * { box-sizing: border-box; margin: 0; padding: 0; }
  html, body { width: 1200px; height: 716px; overflow: hidden; }
  body {
    background: var(--backdrop);
    font-family: "Open Sans", Arial, sans-serif;
    position: relative;
  }
  .card {
    position: absolute;
    top: 204px;
    width: 540px;
    height: 309px;
    border-radius: 4px;
    overflow: hidden;
    background: linear-gradient(160deg, var(--card-black-soft), var(--card-black));
    box-shadow: 0 10px 28px rgba(0,0,0,0.45);
  }
  .card-back { left: 40px; }
  .card-front { left: 620px; }

  .back-wordmark {
    position: absolute;
    inset: 0;
    display: flex;
    align-items: center;
    justify-content: center;
    font-weight: 700;
    font-size: 44px;
    color: var(--muted-grey);
    letter-spacing: 0.5px;
  }

  .glass-silhouettes {
    position: absolute;
    left: 120px;
    top: 30px;
    width: 260px;
    height: 160px;
    border-radius: 50%;
    background: radial-gradient(ellipse at center, rgba(255,255,255,0.05), rgba(255,255,255,0) 70%);
  }
  .front-wordmark {
    position: absolute;
    left: 150px;
    top: 38px;
    font-weight: 700;
    font-size: 40px;
    line-height: 54px;
    color: var(--gold);
    letter-spacing: 0.3px;
  }
  .person {
    position: absolute;
    left: 40px;
    top: 104px;
  }
  .person-name {
    font-weight: 700;
    font-style: italic;
    font-size: 17px;
    line-height: 22px;
    color: var(--gold);
  }
  .person-role {
    font-size: 12px;
    line-height: 16px;
    color: var(--title-grey);
  }
  .wave { position: absolute; left: 0; top: 0; }

  .contact-list {
    position: absolute;
    right: 14px;
    top: 200px;
    list-style: none;
    font-size: 11.5px;
    line-height: 16px;
    color: var(--ink-dark);
  }
  .contact-list li {
    display: flex;
    justify-content: flex-end;
    align-items: center;
    gap: 8px;
    height: 16px;
  }
  .contact-list .icon { width: 11px; height: 11px; flex: none; }
  .contact-list .icon-blank { width: 11px; height: 11px; flex: none; }
  .address {
    position: absolute;
    left: 40px;
    top: 272px;
    font-size: 11.5px;
    line-height: 16px;
    color: var(--ink-dark);
  }
</style>
</head>
<body>

<section class="card card-back" aria-label="Card back">
  <div class="back-wordmark">Velvet Shakers</div>
</section>

<section class="card card-front" aria-label="Card front">
  <div class="glass-silhouettes" role="img" aria-label="Faint cocktail glass silhouettes behind the name"></div>

  <svg class="wave" width="540" height="309" viewBox="0 0 540 309" aria-hidden="true">
    <path d="M0,150 C130,134 240,160 320,160 C400,160 470,144 540,124 L540,136 C470,156 400,172 320,172 C240,172 130,146 0,162 Z" fill="var(--gold)"/>
    <path d="M0,162 C130,146 240,172 320,172 C400,172 470,156 540,136 L540,160 C470,180 400,196 320,196 C240,196 130,170 0,186 Z" fill="var(--card-black)"/>
    <path d="M0,186 C130,170 240,196 320,196 C400,196 470,180 540,160 L540,309 L0,309 Z" fill="var(--gold-light)"/>
    <path d="M0,186 C130,170 240,196 320,196 C400,196 470,180 540,160" fill="none" stroke="var(--gold-deep)" stroke-width="1.5"/>
  </svg>

  <div class="front-wordmark">Velvet Shakers</div>

  <div class="person">
    <p class="person-name">Marcus</p>
    <p class="person-role">Cocktail Maker</p>
  </div>

  <ul class="contact-list">
    <li>0400 118 260
      <svg class="icon" viewBox="0 0 12 12" aria-hidden="true"><path d="M3,1 L5,3.5 L4,5 C4.8,6.6 5.6,7.4 7,8 L8.5,7 L11,9 L9.8,11 C5,10.5 1.5,7 1,2.2 Z" fill="var(--ink-dark)"/></svg>
    </li>
    <li>or 0400 227 391 <span class="icon-blank"></span></li>
    <li>/velvetshakers
      <svg class="icon" viewBox="0 0 12 12" aria-hidden="true"><rect x="1" y="1" width="10" height="10" fill="var(--ink-dark)"/></svg>
    </li>
    <li>info@velvetshakers-example.net
      <svg class="icon" viewBox="0 0 12 12" aria-hidden="true"><rect x="0.5" y="2.5" width="11" height="7" fill="var(--ink-dark)"/><path d="M0.5,2.5 L6,6.5 L11.5,2.5" fill="none" stroke="var(--gold-light)" stroke-width="1"/></svg>
    </li>
    <li>www.velvetshakers-example.net
      <svg class="icon" viewBox="0 0 12 12" aria-hidden="true"><circle cx="6" cy="6" r="5" fill="none" stroke="var(--ink-dark)" stroke-width="1.2"/><ellipse cx="6" cy="6" rx="2" ry="5" fill="none" stroke="var(--ink-dark)" stroke-width="1"/><line x1="1" y1="6" x2="11" y2="6" stroke="var(--ink-dark)" stroke-width="1"/></svg>
    </li>
    <li>
      <svg class="icon" viewBox="0 0 12 12" aria-hidden="true"><path d="M6,11.5 C3,7.5 2,6 2,4.2 A4,4 0 0 1 10,4.2 C10,6 9,7.5 6,11.5 Z" fill="var(--ink-dark)"/><circle cx="6" cy="4.3" r="1.5" fill="var(--gold-light)"/></svg>
    </li>
  </ul>

  <p class="address">PO Box 4821 Seaview, Queensland, Australia</p>
</section>

</body>
</html>
```